Pomme Sauvage Riding School Flyer Design

We need a flyer for our Horse riding school, called Pomme Sauvage Riding School.

At Pomme Sauvage Riding School, Horses and ponies are carefully matched to suit each rider's experience, ability and confidence. I am a Qualified instructor, equipped to train all levels from nervous beginners to the more advanced.

Horse riding is fun! Riders, particularly children, are taught not only skills on the horse, but skills that are integral to good horsemanship and ownership of horses.

We regularly host Ladies Days, Guest Instructors, 1 hour Trail Rides and Pony Ride Days!

We teach people how to interact safely with, and care for horses so they develop a genuine love and respect for the animals and the sport.

In addition to fundamental riding techniques including walk, trot, and canter, we teach our students:
Grooming and Care of horses, Safety around horses, Balance and Co-Ordination, How to saddle up and care for Tack, Responsibility for equipment and horse, Confidence and Confidence Building for all Ages.

Private and group lessons start at 5 years of age upwards.

We recommend children 4 years and under partake in 15 minute pony rides, mainly due to their attention span!

```html
<!DOCTYPE html>
<html lang="en">
<head>
<meta charset="utf-8">
<title>Pomme Sauvage Riding School – Flyer</title>
<link href="https://fonts.googleapis.com/css2?family=Archivo+Narrow:wght@400;700&family=Oswald:wght@600&display=swap" rel="stylesheet">
<style>
  :root {
    --sky-top: #d9b7a6;
    --sky-mid: #d8cbb8;
    --haze: #e9e4d0;
    --water: #7cc2b8;
    --water-deep: #4fa6a6;
    --grass: #7fbf3f;
    --grass-light: #b5dd6a;
    --mane-gold: #e8b53a;
    --mane-amber: #c98a2a;
    --coat-teal: #3d6f6a;
    --title: #f3efe8;
    --title-shadow: rgba(120, 90, 80, 0.35);
    --box-top: #f4f2ea;
    --box-bottom: #c9d7bd;
    --box-text: #1f2320;
    --logo-bg: #f2f2ee;
    --logo-border: #8fbf4a;
    --logo-text: #3a3a3a;
  }
  * { box-sizing: border-box; margin: 0; padding: 0; }
  html, body { width: 1200px; height: 900px; overflow: hidden; background: #ffffff; }
  .flyer {
    position: relative;
    width: 1200px;
    height: 900px;
    overflow: hidden;
    background: linear-gradient(180deg, var(--sky-top) 0%, var(--sky-mid) 35%, var(--haze) 58%, var(--water) 82%, var(--water-deep) 100%);
    font-family: "Archivo Narrow", "Arial Narrow", sans-serif;
  }
  .horse-photo {
    position: absolute;
    left: 0; top: 0;
    width: 560px; height: 900px;
    background:
      radial-gradient(ellipse 55% 45% at 40% 45%, rgba(61,111,106,0.95) 0%, rgba(61,111,106,0.6) 45%, rgba(61,111,106,0) 75%),
      radial-gradient(ellipse 70% 60% at 30% 25%, var(--mane-gold) 0%, var(--mane-amber) 40%, rgba(232,181,58,0) 80%);
    -webkit-mask-image: linear-gradient(90deg, #000 60%, transparent 100%);
            mask-image: linear-gradient(90deg, #000 60%, transparent 100%);
  }
  .grass {
    position: absolute;
    left: 0; bottom: 0;
    width: 1200px; height: 150px;
    background: linear-gradient(180deg, rgba(181,221,106,0) 0%, var(--grass-light) 45%, var(--grass) 100%);
  }
  .headline {
    position: absolute;
    top: 58px; left: 420px;
    width: 700px;
    text-align: center;
    color: var(--title);
    text-shadow: 1px 2px 3px var(--title-shadow);
  }
  .headline h1 {
    font-family: "Oswald", "Arial Narrow", sans-serif;
    font-weight: 600;
    font-size: 64px;
    letter-spacing: -1px;
    line-height: 1;
  }
  .headline p {
    font-size: 17px;
    line-height: 1.25;
    text-transform: uppercase;
    margin-top: 8px;
  }
  .info-box {
    position: absolute;
    left: 440px;
    width: 660px;
    padding: 18px 26px;
    text-align: center;
    text-transform: uppercase;
    font-weight: 700;
    font-size: 17px;
    line-height: 1.35;
    letter-spacing: 0.3px;
    color: var(--box-text);
    background: linear-gradient(180deg, var(--box-top), var(--box-bottom));
    box-shadow: 3px 6px 12px rgba(0,0,0,0.35);
  }
  .info-events { top: 200px; }
  .info-ages { top: 340px; }
  .info-skills { top: 470px; }
  .info-skills .skill-list { margin-top: 14px; }
  .brand-mark {
    position: absolute;
    left: 735px; top: 655px;
    width: 180px; height: 140px;
    display: flex; flex-direction: column; align-items: center; justify-content: center;
    background: var(--logo-bg);
    border: 2px solid var(--logo-border);
    box-shadow: 2px 4px 10px rgba(0,0,0,0.3);
    color: var(--logo-text);
    font-weight: 400;
    text-transform: uppercase;
    text-align: center;
  }
  .brand-name { font-size: 18px; letter-spacing: 3px; line-height: 1.2; }
  .brand-sub { font-size: 10px; letter-spacing: 3px; margin-top: 6px; }
</style>
</head>
<body>
<main class="flyer">
  <div class="horse-photo" role="img" aria-label="Close-up photograph of a horse's head with a flowing golden mane"></div>
  <div class="grass" role="img" aria-label="Green grass meadow along the bottom edge"></div>

  <header class="headline">
    <h1>HORSE RIDING IS FUN!</h1>
    <p>Riders, particularly children, are taught not only skills on the horse,<br>but skills that are integral to good horsemanship and ownership of horses.</p>
  </header>

  <section class="info-box info-events">
    We regularly host Ladies Days, Guest Instructors, 1 hour Trail Rides and Pony Ride Days! We teach people how to interact safely with, and care for horses so they develop a genuine love and respect for the animals and the sport.
  </section>

  <section class="info-box info-ages">
    Private and group lessons start at 5 years of age upwards.<br>
    We recommend children 4 years and under partake in 15 minute pony rides, mainly due to their attention span!
  </section>

  <section class="info-box info-skills">
    <p>In addition to fundamental riding techniques including walk, trot, and canter, we teach our students:</p>
    <p class="skill-list">-- Grooming and care of horses, safety around horses, balance and co-ordination, how to saddle up and care for tack, responsibility for equipment and horse, confidence and confidence building for all ages. --</p>
  </section>

  <div class="brand-mark">
    <span class="brand-name">Pomme Sauvage</span>
    <span class="brand-sub">Riding School</span>
  </div>
</main>
</body>
</html>
```